Marketing Web Site Design for a Mobile CRM Sales Rep App

We are Velmora. We need a web site design to help sell our customizable mobile CRM B2B sales rep app. The site will be used as a sales tool and for lead capture. Our main competitors are trundlo.com and brisketly.com. The site will be about 6 to 10 pages. Take a look at trundlo.com for an example of the type of content that will be on our site.

Target Market(s)

Manufacturers and distributors who have an outside sales force that service retail stores.

Contact Information for Business Card

Malcolm Dunsford
President
3176 Heron Gate Rd #512
Sarasota, Florida 34233

o: 941.507.4419
m: 941.683.1054

e: mdunsford@velmora.com

Selling on the Move

Number of Pages Required

5+ page

Requirements
Must have
• We like how the content on the trundlo.com site is organized. We are not asking that you copy it. Use it for ideas. Here are some pages we need.
• 1. Need a Home Page like: https://www.trundlo.com
• 2. Need an Integration Page like: https://www.trundlo.com/plugin-directory/
• 3. Need a Lead Capture Page like: https://www.trundlo.com/request-a-demo-2/?utm_expid=61724093-27.plwmzqRtU8NNXGJ4ahdkMP.0&utm_referrer=https%3A%2F%2Fwww.trundlo.com%2Fplugin-directory%2F
• 4. Need a Contact Us Page like: https://www.trundlo.com/contact/
• 5. Need a Feature Page like: https://www.trundlo.com/platform-overview/

```html
<!DOCTYPE html>
<html lang="en">
<head>
<meta charset="utf-8">
<title>Velmora – Mobile CRM for B2B Sales Reps</title>
<link href="https://fonts.googleapis.com/css2?family=Montserrat:ital,wght@0,400;0,500;0,600;0,700;1,400&family=Open+Sans:wght@400;600&display=swap" rel="stylesheet">
<style>
:root{
  --ink:#1d1d1f;
  --body:#6d6f73;
  --teal:#35c2e6;
  --green:#8fcf4a;
  --pink:#f0518e;
  --orange:#f9a23a;
  --pale:#eaf7fc;
  --white:#ffffff;
  --line:#e4e4e4;
}
*{margin:0;padding:0;box-sizing:border-box}
html,body{width:1200px;height:5083px;overflow:hidden}
body{position:relative;font-family:"Open Sans",sans-serif;color:var(--ink);background:var(--white)}
.abs{position:absolute}
h1,h2,h3,.head{font-family:"Montserrat",sans-serif}
.btn{position:absolute;display:flex;align-items:center;justify-content:center;color:#fff;font-family:"Montserrat",sans-serif;font-weight:600;font-size:18px;border-radius:30px;background:linear-gradient(90deg,var(--pink),var(--orange))}
.grad-band{background:linear-gradient(110deg,var(--teal) 0%,#6fd0b0 50%,var(--green) 100%)}

/* header */
.site-header{top:0;left:0;width:1200px;height:83px;background:#fff}
.brand{left:78px;top:20px;display:flex;align-items:center;gap:10px;font-family:"Montserrat",sans-serif;font-weight:700;font-size:36px;color:#2b2b2b}
.brand i{width:22px;height:22px;border-radius:50%;background:var(--pink);display:block}
.nav{left:463px;top:32px;display:flex;gap:31px;font-family:"Montserrat",sans-serif;font-size:13px;font-weight:500}
.nav span.on{color:var(--pink)}
.login{left:1010px;top:19px;width:113px;height:46px;font-size:15px}

/* hero */
.hero{top:83px;left:0;width:1200px;height:594px}
.hero h1{left:78px;top:160px;width:620px;font-size:41px;line-height:52px;color:#fff;font-weight:700}
.hero p{left:78px;top:270px;width:540px;font-size:13px;line-height:26px;color:#fff}
.hero-ring{border-radius:50%;border:1px solid rgba(255,255,255,.25)}
.phone{left:790px;top:130px;width:270px;height:500px;border-radius:40px;background:linear-gradient(160deg,#ffffff,#e9f3f6);transform:rotate(8deg);box-shadow:0 10px 40px rgba(0,0,0,.15)}
.dots{left:1155px;top:300px;display:flex;flex-direction:column;gap:11px}
.dots i{width:16px;height:16px;border-radius:50%;border:2px solid #fff;display:block}
.dots i.on{background:var(--pink);border-color:var(--pink)}

/* welcome */
.welcome{left:99px;top:603px;width:573px;height:270px;background:#fff}
.welcome h2{position:absolute;left:36px;top:42px;font-size:36px;font-weight:500}
.welcome p{position:absolute;left:39px;top:105px;width:480px;font-family:"Montserrat",sans-serif;font-style:italic;font-size:13px;line-height:29px;color:#333}

/* features */
.sec-title{left:0;width:1200px;text-align:center;font-size:34px;font-weight:500;line-height:47px}
.feature{width:300px;text-align:center}
.feature .ico{width:94px;height:94px;border-radius:50%;margin:0 auto;display:flex;align-items:center;justify-content:center}
.feature h3{font-size:19px;font-weight:600;margin-top:38px}
.feature p{font-size:13px;line-height:25px;color:var(--body);margin-top:10px}

/* cta */
.cta{top:1720px;left:0;width:1200px;height:365px}
.cta h2{left:78px;top:100px;font-size:36px;line-height:46px;color:#fff;font-weight:500}
.cta-photo{left:540px;top:0;width:660px;height:365px;background:linear-gradient(90deg,rgba(255,255,255,0),#cfd6d4 35%,#9aa6a6 70%,#5e8d8a)}

/* why */
.why{top:2085px;left:0;width:1200px;height:570px;background:var(--pale)}
.why h2{left:78px;top:57px;font-size:34px;font-weight:600}
.card{top:150px;width:241px;height:360px;background:#fff}
.card h3{position:absolute;left:22px;top:38px;font-size:20px;line-height:28px;font-weight:600}
.card p{position:absolute;left:22px;top:100px;font-size:12px;color:var(--body)}
.card .photo{position:absolute;left:0;top:163px;width:241px;height:197px}
.arrow-box{width:45px;height:45px;border:1px solid var(--orange);display:flex;align-items:center;justify-content:center;background:#fff}

/* integrations */
.erp{top:2845px;width:197px;height:90px;border:1px solid var(--line);display:flex;align-items:center;justify-content:center;gap:8px;font-family:"Montserrat",sans-serif;font-weight:600;font-size:20px;color:#2a2a2a}
.erp i{width:16px;height:16px;display:block}

/* trusted */
.trusted{top:2995px;left:0;width:1200px;height:555px}
.trusted h2{left:0;width:1200px;top:60px;text-align:center;color:#fff;font-size:36px;line-height:46px;font-weight:500}
.tile{top:193px;width:246px;height:292px;border-radius:8px;display:flex;align-items:center;justify-content:center;color:#fff;font-family:"Montserrat",sans-serif;font-weight:600;font-size:26px}

/* learn */
.learn h2{left:78px;top:3670px;font-size:38px;line-height:48px;font-weight:500}
.learn h3{left:78px;top:3800px;font-size:30px;color:var(--orange);font-weight:500}
.learn p{left:78px;top:3855px;width:380px;font-size:13px;line-height:28px;color:var(--body)}
.sq{width:43px;height:43px;background:linear-gradient(90deg,var(--orange),var(--pink));display:flex;align-items:center;justify-content:center}

/* join */
.join{top:4100px;left:0;width:1200px;height:515px;background:#eef8fb}
.join-box{left:220px;top:65px;width:655px;height:340px;background:linear-gradient(120deg,var(--green) 0%,#55c9c4 45%,var(--teal) 100%)}
.join-box h2{position:absolute;left:42px;top:85px;font-size:38px;color:#fff;font-weight:700}
.join-box p{position:absolute;left:42px;top:143px;width:500px;font-size:14px;line-height:27px;color:#fff}
.email{left:168px;top:305px;width:409px;height:50px;background:#fff;font-size:12px;color:#999;padding:16px 22px}
.subscribe{left:577px;top:305px;width:208px;height:50px;border-radius:0;font-size:18px}

/* footer */
.footer h4{font-family:"Montserrat",sans-serif;font-size:17px;font-weight:600;position:absolute;top:4665px}
.footer ul{list-style:none;position:absolute;top:4710px;font-size:13px;line-height:33.5px;color:var(--body)}
.social{left:917px;top:4685px;display:flex;gap:10px}
.social i{width:44px;height:44px;border-radius:50%;display:block}
.copy{left:0;width:1200px;top:5030px;text-align:center;font-size:12px;color:#444}
</style>
</head>
<body>

<header class="site-header abs">
  <div class="brand abs"><i></i>Velmora</div>
  <nav class="nav abs"><span class="on">HOME</span><span>INTEGRATION</span><span>LEAD CAPTURE</span><span>FEATURE</span><span>CONTACT US</span></nav>
  <div class="btn login">LOGIN</div>
</header>

<section class="hero abs grad-band">
  <div class="abs hero-ring" style="left:700px;top:-60px;width:560px;height:560px"></div>
  <div class="abs hero-ring" style="left:770px;top:10px;width:420px;height:420px"></div>
  <h1 class="abs">START WITH YOUR FREE ACCOUNT TODAY !</h1>
  <p class="abs">Lorem Ipsum is simply dummy text of the printing and typesetting industry. Lorem Ipsum has been the industry's standard dummy text ever since the .</p>
  <div class="btn" style="left:78px;top:340px;width:238px;height:57px">REQUEST A DEMO</div>
  <div class="phone abs" role="img" aria-label="Smartphone showing the Velmora mobile site"></div>
  <div class="dots abs"><i></i><i class="on"></i><i></i><i></i><i></i></div>
</section>

<div class="welcome abs">
  <h2>Welcome To Velmora</h2>
  <p>Lorem Ipsum is simply dummy text of the printing and typesetting industry. Lorem Ipsum has been the industry's standard dummy text ever since the 1500s, when an unknown printer took a galley of type and scrambled it to make a type specimen book.</p>
</div>
<svg class="abs" style="left:99px;top:893px" width="573" height="28">
  <line x1="0" y1="13" x2="55" y2="13" stroke="#f05a5a" stroke-width="2"/>
  <line x1="71" y1="2" x2="71" y2="22" stroke="#f05a5a" stroke-width="2"/>
  <path d="M65 16 L71 23 L77 16" fill="none" stroke="#f05a5a" stroke-width="2"/>
  <line x1="90" y1="13" x2="573" y2="13" stroke="#f3a45a" stroke-width="1.5"/>
</svg>

<h2 class="sec-title abs" style="top:990px">Velmora is the B2B sales Platform<br>for Brands &amp; Wholesalers</h2>

<div class="feature abs" style="left:130px;top:1135px">
  <div class="ico" style="background:#fdf1df"><svg width="44" height="44" fill="none" stroke="#f2a13a" stroke-width="2"><path d="M6 16h32l-4 22H10z"/><path d="M14 16l6-10M30 16l-6-10"/><path d="M16 22v12M22 22v12M28 22v12"/></svg></div>
  <h3>B2B eCommerce</h3>
  <p>Lorem Ipsum is simply with<br>text the printing and typesetting<br>industry.standard.</p>
</div>
<div class="feature abs" style="left:450px;top:1135px">
  <div class="ico" style="background:#e2f3ee"><svg width="44" height="44" fill="none" stroke="#4aa98a" stroke-width="2"><circle cx="26" cy="16" r="10"/><path d="M26 10v12M23 13h5a2 2 0 010 4h-4a2 2 0 000 4h5"/><path d="M4 34c6-6 12-6 16-2l8-2"/></svg></div>
  <h3>Inside Sale &amp; Support</h3>
  <p>Lorem Ipsum is simply with<br>text the printing and typesetting<br>industry.standard.</p>
</div>
<div class="feature abs" style="left:770px;top:1135px">
  <div class="ico" style="background:#fde3ee"><svg width="44" height="44" fill="none" stroke="#ee5b8f" stroke-width="2"><circle cx="22" cy="12" r="6"/><path d="M12 28c0-6 4-10 10-10s10 4 10 10"/><rect x="8" y="30" width="28" height="8"/></svg></div>
  <h3>Omnichannel Manager</h3>
  <p>Lorem Ipsum is simply with<br>text the printing and typesetting<br>industry.standard.</p>
</div>
<div class="feature abs" style="left:130px;top:1425px">
  <div class="ico" style="background:#e1f4fb"><svg width="44" height="44" fill="none" stroke="#3cb5dc" stroke-width="2"><path d="M6 10h28v22H6z"/><path d="M6 16h28"/><circle cx="32" cy="32" r="7"/><path d="M29 32l2 2 4-4"/></svg></div>
  <h3>Order Taking</h3>
  <p>Lorem Ipsum is simply with<br>text the printing and typesetting<br>industry.standard.</p>
</div>
<div class="feature abs" style="left:450px;top:1425px">
  <div class="ico" style="background:#eef6e2"><svg width="44" height="44" fill="none" stroke="#8dbb4c" stroke-width="2"><rect x="6" y="6" width="32" height="32"/><path d="M6 14h32M14 14v24M22 22h10v10H22z"/></svg></div>
  <h3>Retail Execution</h3>
  <p>Lorem Ipsum is simply with<br>text the printing and typesetting<br>industry.standard.</p>
</div>
<div class="feature abs" style="left:770px;top:1425px">
  <div class="ico" style="background:#fdf1df"><svg width="44" height="44" fill="none" stroke="#f2a13a" stroke-width="2"><circle cx="10" cy="12" r="4"/><circle cx="34" cy="32" r="4"/><path d="M14 12h10a5 5 0 010 10H16a5 5 0 000 10h14" stroke-dasharray="3 3"/></svg></div>
  <h3>Route Accounting</h3>
  <p>Lorem Ipsum is simply with<br>text the printing and typesetting<br>industry.standard.</p>
</div>

<section class="cta abs grad-band">
  <div class="cta-photo abs" role="img" aria-label="Photo of a sales rep using a smartphone at a laptop"></div>
  <h2 class="abs">Ready to talk about your<br>B2B sales? We are.</h2>
  <div class="btn" style="left:78px;top:215px;width:240px;height:50px">REQUEST A DEMO</div>
</section>

<section class="why abs">
  <h2 class="abs">Why Velmora B2B Sales Platform ?</h2>
  <div class="arrow-box abs" style="left:280px;top:265px"><svg width="12" height="14"><path d="M3 2l6 5-6 5" fill="none" stroke="#f9a23a" stroke-width="1.5"/></svg></div>
  <div class="arrow-box abs" style="left:233px;top:315px"><svg width="12" height="14"><path d="M9 2L3 7l6 5" fill="none" stroke="#f9a23a" stroke-width="1.5"/></svg></div>
  <div class="card abs" style="left:362px"><h3>Catalog-centric<br>B2B sales</h3><p>Lorem Ipsum is simply is text.</p><div class="photo" role="img" aria-label="Photo of a woman browsing a product catalog on her phone" style="background:linear-gradient(135deg,#d9cdbb,#8a6d52)"></div><div class="sq abs" style="left:190px;top:163px;width:45px;height:30px"><svg width="14" height="10"><path d="M1 5h11M8 1l4 4-4 4" fill="none" stroke="#fff" stroke-width="1.5"/></svg></div></div>
  <div class="card abs" style="left:618px"><h3>All-in-one<br>platform</h3><div class="photo" role="img" aria-label="Photo of hands paying by card at a laptop" style="background:linear-gradient(135deg,#bdbdbd,#4a4a4a)"></div></div>
  <div class="card abs" style="left:874px"><h3>Unmatched<br>flexibility</h3><div class="photo" role="img" aria-label="Photo of a coffee mug beside a laptop" style="background:linear-gradient(135deg,#9c9c9c,#2d2d2d)"></div></div>
  <div class="card abs" style="left:1128px"><h3>Inherent<br>mobility</h3><div class="photo" role="img" aria-label="Photo of a laptop on a desk" style="background:linear-gradient(135deg,#c7b59a,#5b6c80)"></div></div>
</section>

<h2 class="sec-title abs" style="top:2705px">Seamlessly Integrates With Any<br>ERP or CRM System</h2>
<div class="erp abs" style="left:78px"><i style="background:#1d7ed8"></i>Corvane</div>
<div class="erp abs" style="left:290px"><i style="background:#1e2a3a"></i>Ledgerly</div>
<div class="erp abs" style="left:502px"><i style="background:#27a0db;border-radius:50%"></i>Cloudmere</div>
<div class="erp abs" style="left:712px"><i style="background:#e5301f"></i>Quennor</div>
<div class="erp abs" style="left:925px;font-size:17px"><i style="background:#3a7dc9"></i>Halvern Systems</div>

<section class="trusted abs grad-band">
  <h2 class="abs">Velmora is Loved and Trusted by Enterprise Brands<br>&amp; Wholesalers, Across Industries</h2>
  <div class="tile abs" role="img" aria-label="Photo of a mother holding a sleeping baby" style="left:78px;background:linear-gradient(160deg,#f1ebe6,#c9b8ab)"><span style="margin-top:230px;font-size:18px;color:#24406b">Plumera</span></div>
  <div class="tile abs" role="img" aria-label="Photo of a drinks machine" style="left:344px;background:linear-gradient(160deg,#5c5c5c,#1a1a1a)">fizzora</div>
  <div class="tile abs" role="img" aria-label="Photo of a hotel room interior" style="left:610px;background:linear-gradient(160deg,#6b4a3a,#2a1c17)">Cardwick</div>
  <div class="tile abs" role="img" aria-label="Photo of a surfer facing a big wave" style="left:876px;background:linear-gradient(160deg,#2c6fa6,#0c2f55)">Tidebreak</div>
</section>

<section class="learn">
  <h2 class="abs">Learn More About<br>Transforming B2B Sales</h2>
  <h3 class="abs">White Paper</h3>
  <p class="abs">Lorem Ipsum is simply dummy text of the printing and typesetting industry. Lorem Ipsum has been the industry's standard dummy text ever since the .</p>
  <div class="sq abs" style="left:78px;top:3952px"><svg width="16" height="10"><path d="M15 5H2M5 1L1 5l4 4" fill="none" stroke="#fff" stroke-width="1.5"/></svg></div>
  <div class="sq abs" style="left:125px;top:3952px"><svg width="16" height="10"><path d="M1 5h13M11 1l4 4-4 4" fill="none" stroke="#fff" stroke-width="1.5"/></svg></div>
  <div class="abs" style="left:742px;top:3610px;width:355px;height:340px;background:linear-gradient(160deg,var(--orange),var(--pink))"></div>
  <div class="abs" role="img" aria-label="Photo of a smiling woman holding a phone outdoors" style="left:638px;top:3672px;width:395px;height:366px;background:linear-gradient(135deg,#5f7d4b,#2f4b5c 60%,#a9b6b8)"></div>
</section>

<section class="join abs">
  <div class="abs" style="left:284px;top:232px;width:635px;height:223px;background:var(--green)"></div>
  <div class="join-box abs">
    <h2>JOIN US TODAY</h2>
    <p>Lorem Ipsum is simply dummy text of the printing and typesetting industry. Lorem Ipsum has been the industry's standard.</p>
  </div>
  <div class="email abs">Enter Email *</div>
  <div class="btn subscribe">SUBSCRIBE</div>
</section>

<footer class="footer">
  <h4 style="left:78px">SOLUTIONS</h4>
  <ul style="left:78px"><li>Mobile Order Taking</li><li>Route Accounting DSD</li><li>Retail Execution</li><li>B2B eCommerce</li><li>Inside Sales &amp; Support</li><li>Omnichannel Manager</li><li>Mobile CRM</li></ul>
  <h4 style="left:305px">PLATFORM</h4>
  <ul style="left:305px"><li>Platform Overview</li><li>Enterprise-grade Platform</li><li>Integrations</li><li>Plugin Directory</li><li>3rd Party Apps</li></ul>
  <h4 style="left:530px">INDUSTRY</h4>
  <ul style="left:530px"><li>Fashion Apparel &amp;</li><li>Accessories</li><li>Jewelry &amp; Watches</li><li>Eyewear</li><li>Food &amp; Beverage</li><li>Outdoor &amp; Sporting Goods</li><li>Home &amp; Gifts</li><li>Children's Accessories &amp;</li><li>Toys</li></ul>
  <h4 style="left:768px">SUPPORT</h4>
  <ul style="left:768px"><li>Contact Us</li><li>About Trundlo</li><li>Resources</li><li>Customers</li><li>Partners</li><li>Press &amp; News</li><li>Blog</li><li>Security</li></ul>
  <div class="social abs"><i style="background:#3b5a9a"></i><i style="background:#1da1f2"></i><i style="background:#0e76a8"></i><i style="background:#e62117"></i></div>
  <p class="copy abs">©Velmora - 2019 All Rights Reserved.</p>
</footer>

</body>
</html>
```